Marlow Realty Real Estate Brokerage Recruiting Flyer

We are a real estate brokerage looking to hire more real estate agents. We need to list everything we have to offer as a company so real estate agents will join our company. this is our company website: www.Marlowrealty.example .

100% COMMISSION NO MONTHLY FEE
$450 Flat Transaction FEE

What We Offer:
24/7 Office Access
Free E & O Insurance for 1st Year
Free Online CE and PLE
Free 1,000 Business Cards
Free Professional Social Media Marketing
Free Printing, Scanning, and Copies
Free Buyer and Seller Presentation Packages
Free Filquay Cloud Based Document Management Access
Access to our Internal Brokerage Forum
Company Profit Sharing!
Private Offices Available to Rent

*Lead Generation Software with over 3,000 Leads
*10 Leads to Start
* Free Personal CRM and Website
*Restrictions and Rules apply

Company Address:
4817 Amberfield Road
Suite 512
Fairfax, VA 22194
Phone: 703-555-0147
email: info@marlowrealty.example

Target Market(s)

Real Estate Agents

Industry/Entity Type

Real Estate

Colors
0555a3
ffffff

Requirements
Must have
• 100% COMMISSION NO MONTHLY FEE
$450 Flat Transaction FEE

What We Offer:
24/7 Office Access
Free Online CE and PLE
Free 1,000 Business Cards
Company Profit Sharing!

*10 Leads to Start

Company Address:
4817 Amberfield Road
Suite 512
Fairfax, VA 22194
Phone: 703-555-0147

```html
<!DOCTYPE html>
<html lang="en">
<head>
<meta charset="utf-8">
<title>Marlow Realty – Agent Recruiting Flyer</title>
<link rel="stylesheet" href="https://fonts.googleapis.com/css2?family=Montserrat:ital,wght@0,400;0,500;0,700;1,400&family=Great+Vibes&display=swap">
<style>
  :root{
    --brand-blue:#0555a3;
    --deep-blue:#0a3f80;
    --navy:#072e63;
    --sky:#1a9ae0;
    --teal:#19c3a4;
    --white:#ffffff;
    --footer:#1c232d;
    --logo-navy:#15397a;
  }
  *{margin:0;padding:0;box-sizing:border-box}
  html,body{width:848px;height:1200px;overflow:hidden;background:#fff}
  .flyer{
    position:relative;width:848px;height:1200px;overflow:hidden;
    font-family:'Montserrat',sans-serif;color:var(--white);
    background:linear-gradient(160deg,#0d4f95 0%,var(--deep-blue) 45%,#083a78 100%);
  }
  .hero-photo{
    position:absolute;left:0;top:0;width:848px;height:300px;
    background:linear-gradient(120deg,#ffffff 0%,#f1f2f4 30%,#9ea3ab 60%,#d9dde2 85%,#eef1f4 100%);
  }
  .hero-wave{position:absolute;left:0;top:190px;width:848px;height:140px}
  .brand{
    position:absolute;left:22px;top:48px;display:flex;align-items:center;gap:10px;
    font-weight:500;font-size:34px;letter-spacing:1px;color:var(--logo-navy);
  }
  .brand-mark{width:26px;height:26px;background:var(--logo-navy)}
  .intro{
    position:absolute;left:20px;top:336px;width:820px;
    font-size:19px;line-height:24px;font-weight:400;
  }
  .intro .initial{
    font-family:'Great Vibes',cursive;font-size:84px;line-height:1;
    position:absolute;left:0;top:-28px;
  }
  .intro .line{display:block;white-space:nowrap}
  .intro .l1{padding-left:108px}
  .intro .l2{padding-left:102px}
  .intro .l3{padding-left:86px}
  .perk{position:absolute;top:442px;width:260px;text-align:center}
  .perk svg{display:block;margin:0 auto 10px;width:98px;height:98px}
  .perk-label{font-weight:700;font-size:23.5px;line-height:27px;letter-spacing:.2px}
  .perk.commission{left:19px}
  .perk.monthly{left:294px}
  .perk.flat{left:570px}
  .offer-title{
    position:absolute;left:20px;top:608px;font-weight:700;font-size:54px;line-height:70px;letter-spacing:.5px;white-space:nowrap;
  }
  .offer-title .initial{font-family:'Great Vibes',cursive;font-weight:400;font-size:84px;vertical-align:-4px;margin-right:-10px}
  .offers{position:absolute;top:697px;list-style:none;font-size:20px;line-height:24px}
  .offers.left{left:21px;width:405px}
  .offers.right{left:426px;width:414px}
  .offers li{position:relative;padding-left:40px;margin-bottom:10px}
  .offers.right li{padding-left:42px}
  .offers li::before{
    content:"";position:absolute;left:4px;top:4px;width:15px;height:15px;background:var(--white);
  }
  .notes{position:absolute;left:21px;top:952px;font-style:italic;font-size:15px;line-height:18px}
  .notes .gap{margin-left:18px}
  .footer{
    position:absolute;left:0;top:1011px;width:848px;height:167px;background:var(--footer);
  }
  .footer-strip{position:absolute;left:0;top:1178px;width:848px;height:22px;background:var(--navy)}
  .address{position:absolute;left:23px;top:26px;font-size:21px;line-height:24px}
  .address h2{font-weight:700;font-size:20px;margin-bottom:12px}
  .address .row{display:flex;gap:6px}
  .address .indent{padding-left:21px}
  .address svg{width:15px;height:18px;margin-top:3px;flex:none}
  .site{
    position:absolute;left:328px;top:63px;width:230px;height:42px;
    background:linear-gradient(90deg,#0a7cf0,var(--teal));
    display:flex;align-items:center;justify-content:center;gap:5px;
    font-weight:700;font-size:13px;color:var(--white);white-space:nowrap;
  }
  .site svg{width:12px;height:12px;flex:none}
  .contact{position:absolute;right:20px;top:62px;text-align:right;font-size:19px;line-height:24px}
  .contact .row{display:flex;justify-content:flex-end;align-items:center;gap:6px;margin-bottom:11px;white-space:nowrap}
  .contact svg{width:14px;height:18px}
</style>
</head>
<body>
<main class="flyer">
  <div class="hero-photo" role="img" aria-label="Photo of an agent in a suit signing papers beside a model house on a glass desk"></div>
  <svg class="hero-wave" viewBox="0 0 848 140" preserveAspectRatio="none" aria-hidden="true">
    <defs>
      <linearGradient id="edge" x1="0" x2="1">
        <stop offset="0" stop-color="#1a9ae0"/><stop offset="1" stop-color="#19c3a4"/>
      </linearGradient>
    </defs>
    <path d="M0 71 C250 115 550 115 848 14 L848 140 L0 140Z" fill="#072e63"/>
    <path d="M0 95 C300 130 600 110 848 20 L848 140 L0 140Z" fill="#0d4f95"/>
    <path d="M0 95 C300 130 600 110 848 20" fill="none" stroke="url(#edge)" stroke-width="4"/>
  </svg>

  <div class="brand"><span class="brand-mark"></span>Marlow Realty</div>

  <p class="intro">
    <span class="initial">W</span>
    <span class="line l1">e are a real estate brokerage looking to hire more real estate agents.</span>
    <span class="line l2">We need to list everything we have to offer as a company&nbsp; so real estate</span>
    <span class="line l3">agents will&nbsp; join our company.</span>
  </p>

  <section class="perk commission">
    <svg viewBox="0 0 98 98" aria-hidden="true">
      <circle cx="49" cy="49" r="46" fill="none" stroke="#fff" stroke-width="3.5"/>
      <path d="M22 34h54v8a7 7 0 0 0 0 14v8H22v-8a7 7 0 0 0 0-14z" fill="none" stroke="#1a8fe6" stroke-width="5"/>
      <text x="49" y="57" text-anchor="middle" font-family="Montserrat,sans-serif" font-weight="700" font-size="20" fill="#19c3a4">%</text>
    </svg>
    <div class="perk-label">100% COMMISSION</div>
  </section>
  <section class="perk monthly">
    <svg viewBox="0 0 98 98" aria-hidden="true">
      <circle cx="49" cy="49" r="46" fill="none" stroke="#fff" stroke-width="3.5"/>
      <rect x="22" y="27" width="44" height="40" fill="none" stroke="#1a8fe6" stroke-width="4"/>
      <path d="M22 38h44" stroke="#1a8fe6" stroke-width="4"/>
      <rect x="28" y="46" width="6" height="6" fill="#1a8fe6"/><rect x="38" y="46" width="6" height="6" fill="#1a8fe6"/>
      <rect x="28" y="56" width="6" height="6" fill="#1a8fe6"/>
      <circle cx="65" cy="66" r="11" fill="none" stroke="#19c3a4" stroke-width="4"/>
      <path d="M16 16L82 82" stroke="#fff" stroke-width="3.5"/>
    </svg>
    <div class="perk-label">NO MONTHLY FEE</div>
  </section>
  <section class="perk flat">
    <svg viewBox="0 0 98 98" aria-hidden="true">
      <circle cx="49" cy="49" r="46" fill="none" stroke="#fff" stroke-width="3.5"/>
      <text x="46" y="62" text-anchor="middle" font-family="Montserrat,sans-serif" font-weight="500" font-size="42" fill="#1a8fe6">$</text>
      <path d="M33 73h30M57 67l7 6-7 6" fill="none" stroke="#19c3a4" stroke-width="4"/>
    </svg>
    <div class="perk-label">$450 FLAT<br>TRANSACTION FEE</div>
  </section>

  <h1 class="offer-title"><span class="initial">W</span>hat We Offer :</h1>

  <ul class="offers left">
    <li>24/7 Office Access</li>
    <li>Free E &amp; O Insurance for 1st Year</li>
    <li>Free Online CE and PLE</li>
    <li>Free 1,000 Business Cards</li>
    <li>Free Professional Social Media Marketing</li>
    <li>Free Printing, Scanning, and Copies</li>
  </ul>
  <ul class="offers right">
    <li>Free Buyer and Seller Presentation Packages</li>
    <li>Free Filquay Cloud Based Document Management Access</li>
    <li>Access to our Internal Brokerage Forum</li>
    <li>Company Profit Sharing!</li>
    <li>Private Offices Available to Rent</li>
  </ul>

  <p class="notes">
    *Lead Generation Software with over 3,000 Leads<br>
    *10 Leads to Start<span class="gap">* Free Personal CRM and Website</span><br>
    *Restrictions and Rules apply
  </p>

  <footer class="footer">
    <div class="address">
      <h2>Company Address:</h2>
      <div class="row">
        <svg viewBox="0 0 15 18" aria-hidden="true"><path d="M7.5 17C3 11 1.5 8.5 1.5 6.5a6 6 0 0 1 12 0c0 2-1.5 4.5-6 10.5z" fill="none" stroke="#fff" stroke-width="1.4"/><circle cx="7.5" cy="6.5" r="2.2" fill="none" stroke="#fff" stroke-width="1.4"/></svg>
        <span>4817 Amberfield Road</span>
      </div>
      <div class="indent">Suite 512</div>
      <div class="indent">Fairfax, VA 22194</div>
    </div>
    <div class="site">
      <svg viewBox="0 0 14 14" aria-hidden="true"><circle cx="7" cy="7" r="6" fill="none" stroke="#fff" stroke-width="1.3"/><ellipse cx="7" cy="7" rx="2.6" ry="6" fill="none" stroke="#fff" stroke-width="1.1"/><path d="M1 7h12" stroke="#fff" stroke-width="1.1"/></svg>
      <span>www.Marlowrealty.example</span>
    </div>
    <div class="contact">
      <div class="row">
        <svg viewBox="0 0 14 18" aria-hidden="true"><rect x="2" y="1" width="10" height="16" rx="1.5" fill="none" stroke="#fff" stroke-width="1.4"/><path d="M6 14h2" stroke="#fff" stroke-width="1.4"/></svg>
        <span>703-555-0147</span>
      </div>
      <div class="row">
        <svg viewBox="0 0 16 12" style="width:16px;height:12px" aria-hidden="true"><rect x="1" y="1" width="14" height="10" fill="none" stroke="#fff" stroke-width="1.3"/><path d="M1 1l7 6 7-6" fill="none" stroke="#fff" stroke-width="1.3"/></svg>
        <span>info@marlowrealty.example</span>
      </div>
    </div>
  </footer>
  <div class="footer-strip"></div>
</main>
</body>
</html>
```